Very Simple Web Redesign Project - Using Photoshop

Required is a very simple website home page redesign for the following site: http://www.kestrelslateworks.com.au/
I require this as a Photoshop design.
The basic look and feel of the site needs to remain.
Specifically the colours don't need to be changed.
The positioning of the site is currently correct for the target market.
The site does not need to be made super slick looking. Just upgraded to a new version.
The current text can all be used.
The only menus necessary are a horizontal menu at the top, and a simple horizontal text menu at the bottom of the page. Do NOT retain the vertical menu on the home page (having the items "Our Gallery", "Our Services", "Enquire Now").
Give the horizontal menu the following items:
Home | Slate Roof Repairs | Slate Reroofing | Slate Roof Benefits | Other Services | Photo Gallery | FAQ's | Free Quote | Contact Us
The picture of the house at the top RHS of the page needs to be reduced in size by approx 50% and moved to the top LHS of the page.
Please place the following text into the top of the page:
"Call Now: 0427 618 302"
Keep the four pictures on the home page layout. Some larger images attached.
Thanks,
Ned
Updates
Hi,
Thanks for all the designs.
I am working with my client to get which one they like the most.
Thanks,
Ned

```html
<!DOCTYPE html>
<html lang="en">
<head>
<meta charset="utf-8">
<title>Kestrel Slateworks – Slate Roof Specialists</title>
<link rel="stylesheet" href="https://fonts.googleapis.com/css2?family=Arimo:wght@400;700&family=Open+Sans:wght@600&display=swap">
<style>
:root{
  --bg-top:#1f4a02;
  --bg-low:#88b06a;
  --header:#33601b;
  --triangle:#8ab56c;
  --nav:#4e8f2b;
  --panel:#1f4a0c;
  --page:#f1f1f1;
  --heading:#1f4a00;
  --text:#3c6a12;
  --cloud:#8aa57a;
  --rule:#cfcfcf;
  --white:#ffffff;
}
*{margin:0;padding:0;box-sizing:border-box}
html,body{width:1200px;height:919px;overflow:hidden}
body{
  font-family:"Arimo",Arial,sans-serif;
  background:linear-gradient(var(--bg-top) 0 171px,var(--bg-low) 171px);
  position:relative;
}
.site{position:absolute;left:145px;top:0;width:910px;height:919px}
.header{position:absolute;left:0;top:0;width:910px;height:141px;background:var(--header);overflow:hidden}
.header svg{position:absolute;left:0;top:0}
.brand{
  position:absolute;left:32px;top:82px;
  font-family:"Open Sans",Arial,sans-serif;font-weight:600;
  font-size:44px;line-height:1;color:var(--white);letter-spacing:-.5px;white-space:nowrap;
}
.registration{position:absolute;right:20px;top:115px;font-size:11.5px;color:var(--white);white-space:nowrap}
.main-nav{
  position:absolute;left:0;top:141px;width:910px;height:30px;background:var(--nav);
  display:flex;justify-content:space-between;align-items:center;padding:0 21px 0 33px;
  list-style:none;
}
.main-nav a{color:var(--white);text-decoration:none;font-size:13.5px;white-space:nowrap}
.hero{position:absolute;left:0;top:171px;width:910px;height:336px}
.hero-photo{position:absolute;left:0;top:0;width:612px;height:336px;
  background:linear-gradient(160deg,#4d6a2c 0%,#6a4c5c 35%,#7d5566 60%,#8a6b5a 85%,#c8b49a 100%)}
.quote-call{position:absolute;left:0;top:269px;width:395px;height:45px;background:rgba(20,30,15,.72);
  color:var(--white);display:flex;align-items:center;padding-left:34px;gap:10px;white-space:nowrap;overflow:hidden}
.quote-call .label{font-size:18px;line-height:1}
.quote-call .phone{font-size:28px;line-height:1}
.intro{position:absolute;left:612px;top:0;width:298px;height:336px;
  background:linear-gradient(170deg,#2a5a14,var(--panel) 60%,#2f5e18)}
.intro h1{position:absolute;left:11px;top:27px;font-weight:400;font-size:28px;color:var(--white);letter-spacing:-.2px;white-space:nowrap}
.intro p{position:absolute;left:11px;top:70px;width:272px;font-size:11.3px;line-height:15.2px;color:var(--white);letter-spacing:.3px}
.thumb{position:absolute;top:206px;height:122px}
.thumb-one{left:11px;width:148px;background:linear-gradient(135deg,#9a4a38 0%,#7f8a96 35%,#6f7886 100%)}
.thumb-two{left:167px;width:131px;background:linear-gradient(135deg,#4c7a2c 0%,#9d5a44 40%,#616a78 100%)}
.content{position:absolute;left:0;top:507px;width:910px;height:412px;background:var(--page)}
.column{position:absolute;top:21px;font-size:12px;line-height:13.7px;color:var(--text)}
.column h2{font-size:13.5px;color:var(--heading);margin-bottom:10px;font-weight:700;white-space:nowrap}
.column p{margin-bottom:13.7px}
.col-about{left:34px;width:272px}
.col-services{left:331px;width:272px}
.col-area{left:625px;width:264px}
.divider{position:absolute;top:47px;width:1px;height:252px;background:var(--rule)}
.services-list{list-style:none;margin-bottom:13.7px}
.services-list li{position:relative;padding-left:10px}
.services-list li::before{content:"";position:absolute;left:1px;top:5px;border-left:4px solid var(--text);border-top:3px solid transparent;border-bottom:3px solid transparent}
.read-more{color:var(--heading);font-weight:700;text-decoration:none}
.tag-cloud{position:relative;height:180px;margin-top:8px;color:var(--cloud);font-weight:700}
.tag-cloud span{position:absolute;white-space:nowrap;line-height:1}
.footer-rule{position:absolute;left:34px;top:338px;width:854px;height:1px;background:var(--heading)}
.footer{position:absolute;left:34px;top:343px;width:854px;display:flex;justify-content:space-between;font-size:9.5px;color:var(--heading);letter-spacing:.8px;white-space:nowrap}
.footer-nav{display:flex;gap:9px;list-style:none}
.footer-nav a{color:var(--heading);text-decoration:none}
</style>
</head>
<body>
<div class="site">
  <header class="header">
    <svg width="910" height="141" aria-hidden="true"><polygon points="0,141 139,0 291,141" fill="var(--triangle)"/></svg>
    <div class="brand">Kestrel Slateworks</div>
    <div class="registration">ABN 47 306 918 225 &nbsp;&nbsp;Lic. No. 238411C</div>
  </header>
  <ul class="main-nav">
    <li><a href="#">Home</a></li>
    <li><a href="#">Slate Roof Repairs</a></li>
    <li><a href="#">Slate Reroofing</a></li>
    <li><a href="#">Slate Roof Benefits</a></li>
    <li><a href="#">Other Services</a></li>
    <li><a href="#">Photo Gallery</a></li>
    <li><a href="#">FAQs</a></li>
    <li><a href="#">Free Quote</a></li>
    <li><a href="#">Contact Us</a></li>
  </ul>
  <section class="hero">
    <div class="hero-photo" role="img" aria-label="Photo of a conical slate roof among garden trees"></div>
    <div class="quote-call"><span class="label">Call now for a quote</span><span class="phone">0427 618 302</span></div>
    <div class="intro">
      <h1>Slate roof specialists</h1>
      <p>At Kestrel Slateworks we specialize in the upkeep, maintenance, repair and replacement of all types of slate roof as well as wood shingles. We can track down the leak that just won't go away or give your house a complete re-roof. We can also provide all your guttering needs.</p>
      <div class="thumb thumb-one" role="img" aria-label="Photo of a slate roof beside a brick wall and downpipe"></div>
      <div class="thumb thumb-two" role="img" aria-label="Photo of a slate roof on a bay window house"></div>
    </div>
  </section>
  <main class="content">
    <div class="column col-about">
      <h2>About Kestrel Slateworks</h2>
      <p>Kestrel Slateworks is a small company and as such we do not have the overheads that larger companies do. Quality work and attention to detail are our trademark.</p>
      <p>All photos on this web site consist of work which I have personally done. The above photos provide at a quick glance a reasonable cross section of the type of work I do.</p>
      <p>By clicking on the photo gallery link you can see other work including some before and after shots.</p>
      <p>Feel free to call at your earliest convenience to organise an obligation-free quote or click on the contact us link and send us an e-mail.</p>
    </div>
    <div class="divider" style="left:317px"></div>
    <div class="column col-services">
      <h2>Our Services</h2>
      <p>At Kestrel Slateworks we provide a variety of services in the upkeep, maintenance and or replacement of your slate and wood shingle roof.</p>
      <ul class="services-list">
        <li>tracking down and handling leaks</li>
        <li>replacement of broken slate</li>
        <li>re-securing slipped slate</li>
        <li>replacement of roofing valleys</li>
        <li>replacement and or maintenance of all types of ridge capping</li>
        <li>gutter, downpipe and gutter guard installation and replacement</li>
        <li>re-nailing of slate</li>
        <li>re-roofing in new or second hand slate</li>
      </ul>
      <p>We are also able to handle all your wood roofing shingle requirements. <a class="read-more" href="#">Read more</a>...</p>
    </div>
    <div class="divider" style="left:613px"></div>
    <div class="column col-area">
      <h2>Sydney Service Area</h2>
      <p>We service all inner city suburbs of Sydney roughly covering an area encompassing Gordon to Epping, Mosman to Bondi, Coogee to Kogarah and Kingsgrove to Burwood and Concord.</p>
      <div class="tag-cloud">
        <span style="left:11px;top:3px;font-size:13px">Roof Restoration</span>
        <span style="left:68px;top:9px;font-size:22px">Slate</span>
        <span style="left:130px;top:13px;font-size:13px">Wood Shingles</span>
        <span style="left:28px;top:28px;font-size:23px">Roof Tiles</span>
        <span style="left:3px;top:50px;font-size:13px">Guttering</span>
        <span style="left:125px;top:46px;font-size:17px">Ridge Capping</span>
        <span style="left:62px;top:66px;font-size:13px">Roof Repair</span>
        <span style="left:101px;top:77px;font-size:23px">Welsh Slate</span>
        <span style="left:20px;top:97px;font-size:13px">Downpipe Installation</span>
        <span style="left:40px;top:114px;font-size:17px">Quality Workmanship</span>
        <span style="left:140px;top:129px;font-size:13px">Leaking Roof</span>
        <span style="left:10px;top:145px;font-size:17px">Long Lasting Roof</span>
        <span style="left:83px;top:163px;font-size:13px">Roof Maintenance</span>
      </div>
    </div>
    <div class="footer-rule"></div>
    <footer class="footer">
      <span>© 2011 Kestrel Slateworks</span>
      <ul class="footer-nav">
        <li><a href="#">Home</a></li>
        <li><a href="#">Slate Roof Repairs</a></li>
        <li><a href="#">Slate Reroofing</a></li>
        <li><a href="#">Slate Roof Benefits</a></li>
        <li><a href="#">Other Services</a></li>
        <li><a href="#">Photo Gallery</a></li>
        <li><a href="#">FAQs</a></li>
        <li><a href="#">Free Quote</a></li>
        <li><a href="#">Contact Us</a></li>
      </ul>
    </footer>
  </main>
</div>
</body>
</html>
```